Bakery Replacement Lighted Sign Face

We are opening a new bakery that sells only cakes. The name is "The Frosted Parlor." We are replacing the current sign face with a new look that states our name and makes a bold statement of fun. We will be known for having 101 cakes that are always ready for immediate pickup or delivery. Our colors are pink, orange, and lime green. An image is provided to see the colors.

Target Market(s)

people who buy cakes for parties and all other occasions

Industry/Entity Type

Cakes

Font styles to use
Other font styles liked:
• look at the logo and file for the main font name

Colors
59FF00
82FF00
B8FF75
E3FFCB
F4FFEA
F0912C
F2A743
F7CA91
FBE8D2
FDF5EE
EB3D1F
EC4F4E
F09395
F8D3D4
FCEDEE

Requirements
Must have
• The name of the bakery. Logo can be used as is or changed as shown in one of the uploaded PDFs. Must use either pink, orange, lime green, white, or black. We prefer a bright pink background with white lettering as our first choice, but are willing to be open minded to see all creative concepts. Also the sign is 14 feet long and 42 inches tall so the artwork must fit within those boundaries. Also keep in mind the sign does have a 4 inch black frame. So the graphics area is actually 13 feet 2 inches by 3 feet. Also, in the attached pdf that shows a rough possible layout, the words "101 cakes to go" is on the sign. It is NOT a must. Only use the wording if it adds to your design.
Nice to have
• You are welcome to add additional stars or other fun graphics that could look good.
Should not have
• No images of cakes or other bakery products.

```html
<!DOCTYPE html>
<html lang="en">
<head>
<meta charset="utf-8">
<title>The Frosted Parlor – Sign Face</title>
<link href="https://fonts.googleapis.com/css2?family=Fredoka:wght@600&display=swap" rel="stylesheet">
<style>
  :root {
    --backdrop: #f2f2f2;
    --parlor-pink: #cd3a87;
    --lime: #cee4a2;
    --orange: #f59a58;
    --white: #ffffff;
    --shadow: rgba(0, 0, 0, 0.35);
  }
  html, body {
    margin: 0;
    padding: 0;
    width: 1200px;
    height: 402px;
    overflow: hidden;
    background: var(--backdrop);
  }
  .sign {
    position: absolute;
    left: 112px;
    top: 79px;
    width: 976px;
    height: 244px;
    box-shadow: 4px 6px 8px var(--shadow);
  }
  .sign svg { display: block; }
  .sign-text {
    font-family: "Fredoka", sans-serif;
    font-weight: 600;
  }
  .bg { fill: var(--parlor-pink); }
  .dot-white { fill: var(--white); }
  .dot-lime { fill: var(--lime); }
  .dot-orange { fill: var(--orange); }
  .brand-name { fill: var(--white); }
  .count { fill: var(--parlor-pink); }
  .to-go { fill: var(--white); }
</style>
</head>
<body>
  <div class="sign">
    <svg width="976" height="244" viewBox="0 0 976 244" xmlns="http://www.w3.org/2000/svg">
      <defs>
        <clipPath id="sign-area"><rect width="976" height="244"/></clipPath>
      </defs>
      <g clip-path="url(#sign-area)">
        <rect class="bg" width="976" height="244"/>

        <!-- decorative dots -->
        <circle class="dot-lime" cx="750" cy="4" r="166"/>
        <circle class="dot-orange" cx="968" cy="226" r="73"/>
        <circle class="dot-lime" cx="15" cy="253" r="65"/>
        <circle class="dot-white" cx="541" cy="34" r="23.5"/>
        <circle class="dot-lime" cx="946" cy="84" r="12.5"/>
        <circle class="dot-orange" cx="599" cy="147" r="16"/>
        <circle class="dot-white" cx="22" cy="158" r="8"/>
        <circle class="dot-white" cx="78" cy="181" r="13"/>
        <circle class="dot-white" cx="121" cy="238" r="18"/>

        <!-- bakery name -->
        <g class="sign-text brand-name" text-anchor="middle">
          <text x="282" y="125" font-size="66">The Frosted</text>
          <text x="282" y="170" font-size="40" letter-spacing="8">Parlor</text>
        </g>

        <!-- offer -->
        <g class="sign-text" text-anchor="middle">
          <text class="count" x="750" y="97" font-size="100">101</text>
          <text class="count" x="750" y="144" font-size="48">cakes</text>
          <text class="to-go" x="750" y="229" font-size="68">TO GO</text>
        </g>
      </g>
    </svg>
  </div>
</body>
</html>
```